Business card for Tolvery Anesthesia LLC

This is for a business care for Tolvery Anesthesia LLC. Dr. Lisbeth Tolvery, CRNA, DNAP is the sole provider in the LLC. Business address is 4718 N Brackley Street,
Oakhaven, PA 17342
CRNA stands for certified registered nurse anesthetist
"Keeping you safe and comfortable"
I plan to give this business card to the patients that I provide anesthesia to.
Creative design that ties into Anesthesia. Calm soothing colors.

Target Market(s)

Business card for my patients.

Industry/Entity Type

Medicine

Contact Information for Business Card

Creative, professional, eye catching

Logo Text

Tolvery Anesthesia

Font styles to use
Serif
Script

Colors

Designer to choose colors to be used in the design.

Requirements
Must have
• Tolvery Anesthesia
• Dr. Lisbeth Tolvery, CRNA, DNAP
• tolvery.anesthesia@ quillmail.net
Nice to have
• "Keeping you safe and comfortable"
Should not have
• phone number

```html
<!DOCTYPE html>
<html lang="en">
<head>
<meta charset="utf-8">
<title>Tolvery Anesthesia — Business Card</title>
<link rel="stylesheet" href="https://fonts.googleapis.com/css2?family=Jost:wght@600&family=Lato:wght@300;400&family=Cormorant+Garamond:wght@500&display=swap">
<style>
  :root {
    --backdrop: #bdbdbd;
    --card-light: #efefef;
    --card-navy: #3c5580;
    --ink-navy: #2f4a78;
    --ink-grey: #4a4a4a;
    --teal: #3fa9c6;
    --coral: #e1553a;
    --wine: #6b1f2a;
    --scrub: #4fb3cc;
    --white: #ffffff;
  }
  * { margin: 0; padding: 0; box-sizing: border-box; }
  html, body { width: 1200px; height: 1043px; overflow: hidden; }
  body { background: var(--backdrop); position: relative; font-family: "Lato", sans-serif; }

  .card {
    position: absolute;
    top: 369px;
    width: 550px;
    height: 305px;
    box-shadow: 0 2px 6px rgba(0,0,0,0.18);
  }
  .card--front { left: 30px; background: var(--card-light); }
  .card--back { left: 620px; background: var(--card-navy); }

  .plus { position: absolute; width: 14px; height: 14px; }

  .front__name {
    position: absolute; top: 64px; width: 100%; text-align: center;
    font-family: "Jost", sans-serif; font-weight: 600; font-size: 22px;
    color: var(--ink-navy); letter-spacing: 0.3px;
  }
  .front__email {
    position: absolute; top: 98px; width: 100%; text-align: center;
    font-size: 13.5px; color: var(--ink-grey);
  }
  .front__wordcloud {
    position: absolute; top: 128px; left: 170px; width: 210px; height: 66px;
    border-radius: 33px;
    background: radial-gradient(ellipse at center, var(--wine) 0%, #9a4a3c 45%, rgba(200,150,130,0.35) 75%, rgba(239,239,239,0) 100%);
  }
  .brand {
    font-family: "Cormorant Garamond", serif; font-weight: 500;
    text-transform: uppercase; letter-spacing: 1.5px;
  }
  .front__brand {
    position: absolute; top: 212px; width: 100%; text-align: center;
    font-size: 23px; color: var(--teal);
  }
  .front__tagline {
    position: absolute; top: 243px; width: 100%; text-align: center;
    font-size: 13.5px; font-weight: 300; color: var(--ink-grey);
  }

  .back__illustration {
    position: absolute; top: 38px; left: 190px; width: 170px; height: 162px;
    border-radius: 70px 70px 6px 6px;
    background: linear-gradient(180deg, #5cc0d6 0%, #e9c596 45%, #45a9c4 100%);
    opacity: 0.9;
  }
  .back__rule {
    position: absolute; top: 200px; left: 179px; width: 195px; height: 3px;
    background: var(--white);
  }
  .back__brand {
    position: absolute; top: 222px; width: 100%; text-align: center;
    font-size: 22px; letter-spacing: 3px; color: var(--white);
  }
  .back__address {
    position: absolute; top: 255px; width: 100%; text-align: center;
    font-size: 13.5px; color: var(--white);
  }
</style>
</head>
<body>
  <section class="card card--front">
    <svg class="plus" style="left:24px;top:25px" viewBox="0 0 14 14" aria-hidden="true"><path d="M7 1v12M1 7h12" stroke="var(--coral)" stroke-width="3" stroke-linecap="round"/></svg>
    <h1 class="front__name">Dr. Lisbeth Tolvery, CRNA, DNAP</h1>
    <p class="front__email">tolvery.anesthesia@ quillmail.net</p>
    <div class="front__wordcloud" role="img" aria-label="Word cloud of anesthesia terms: anesthesia, surgery, medicine, hospital"></div>
    <p class="brand front__brand">Tolvery Anesthesia</p>
    <p class="front__tagline">Keeping You Safe And Comfortable</p>
    <svg class="plus" style="left:511px;top:266px" viewBox="0 0 14 14" aria-hidden="true"><path d="M7 1v12M1 7h12" stroke="var(--teal)" stroke-width="3" stroke-linecap="round"/></svg>
  </section>

  <section class="card card--back">
    <svg class="plus" style="left:510px;top:25px" viewBox="0 0 14 14" aria-hidden="true"><path d="M7 1v12M1 7h12" stroke="var(--coral)" stroke-width="3" stroke-linecap="round"/></svg>
    <div class="back__illustration" role="img" aria-label="Illustration of an anesthetist in scrub cap and mask beside a syringe"></div>
    <div class="back__rule"></div>
    <p class="brand back__brand">Tolvery Anesthesia</p>
    <p class="back__address">4718 N Brackley Street, Oakhaven, PA 17342</p>
    <svg class="plus" style="left:27px;top:268px" viewBox="0 0 14 14" aria-hidden="true"><path d="M7 1v12M1 7h12" stroke="var(--teal)" stroke-width="3" stroke-linecap="round"/></svg>
  </section>
</body>
</html>
```